Redesign this Sydney Chocolatier Website

We are looking for a redesign of this websites home page and product pages.

https://marlowconfections.com.au/

Marlow Confections have been making handmade chocolates in Sydney Australia since 1932 they specialize in making hand made chocolates without additives, without palm oil and using all-natural ingredients.

We are looking to rebrand the company to reposition the brand in the high-quality chocolate gifts and hampers market as such they have launched products to tackle this market.

https://marlowconfections.com.au/hampers-2/

Some of the players in this market that we would like to compete with are

https://www.thegiftcrategallery.com.au/

https://www.brindlecocoa.com.au/

https://www.chocolate.vesperine.com/

The website is currently built on Kavo Woo-commerce and though it looks decent in our opinion the home page is a little busy and does not convey the quality of the brand.

We are looking for something cleaner that will perform great especially on mobiles.

Target Market(s)

Families and business owners 40+ affluent we specialise in luxury chocolates hampers and chocolate gifts the current look lacks the high end look.

Number of Pages Required

2 page

Font styles to use
Script

Requirements
Must have
• Good SEO Footer, easy to navigate, cleaner than the original design, presents well on mobile devices, plant of room for copy I have included a copy doc with the actual home page copy.
Nice to have
• Something more stylish and high end looking that will appeal to the target market. clean navigation and easy to use that again translates well to mobile, you can use divs and read mores to declutter the long SEO texts see suggested copy doc (you do not have to use all of this
Should not have
• Less cluttered more stylish design than the original website

```html
<!DOCTYPE html>
<html lang="en">
<head>
<meta charset="utf-8">
<title>Chocolate Gift Hampers – Marlow Confections</title>
<link href="https://fonts.googleapis.com/css2?family=Roboto:wght@400;500&family=Hind:wght@400;500&family=Prata&display=swap" rel="stylesheet">
<style>
:root{
  --brown:#744c42;--black:#0d0d0d;--gold:#c0a46e;--gold-text:#b08a52;--nav-gold:#cfae6c;
  --maroon:#7b2a1f;--bg:#efeff2;--white:#fff;--ink:#222;--muted:#555;--green:#3aa43a;--dark:#3a3a3a;--star:#f5a623;
}
*{box-sizing:border-box;margin:0;padding:0}
html,body{width:676px;height:1200px;overflow:hidden;background:var(--bg)}
.page{width:1440px;height:2556px;transform:scale(.469444);transform-origin:0 0;position:relative;font-family:Roboto,sans-serif;color:var(--ink);background:var(--bg)}
.abs{position:absolute}
.topbar{left:0;top:0;width:1440px;height:78px;background:var(--brown);color:#fff;font-size:23px}
.topbar span{position:absolute;top:26px;display:flex;align-items:center;gap:8px}
.badge{width:22px;height:22px;border-radius:50%;background:var(--gold);font-size:14px;font-style:normal;display:inline-flex;align-items:center;justify-content:center;margin:-20px -4px 0 -14px}
.mainnav{left:0;top:78px;width:1440px;height:100px;background:var(--black)}
.brand{left:120px;top:26px;color:var(--gold);font-family:Prata,serif;font-size:44px;line-height:1}
.menu{right:120px;top:36px;display:flex;gap:38px;color:var(--nav-gold);font-size:23px;font-weight:500}
.menu i{font-style:normal;font-size:14px;margin-left:8px}
.product{left:120px;top:228px;width:1200px;height:500px;background:#fff}
.cats{left:0;top:14px;width:270px;font-family:Hind,sans-serif;color:#fff;font-size:19px}
.cats div{height:50px;padding:14px 10px;border-bottom:1px solid rgba(255,255,255,.35);position:relative}
.cats .head{background:var(--gold);text-align:center;font-size:21px}
.cats .g{background:var(--gold)}
.cats .d{background:var(--dark)}
.cats b{position:absolute;right:12px;top:18px;font-size:12px;font-weight:400}
.hero{left:299px;top:14px;width:450px;height:300px;background:linear-gradient(160deg,#f4eee6,#cbb7e0 55%,#e9e4dc)}
.dots{left:480px;top:336px;display:flex;gap:16px}
.dots i{width:10px;height:10px;border-radius:50%;background:#bbb;display:block}
.dots i.on{background:#b06a10}
.thumbs{left:306px;top:368px;display:flex;gap:12px}
.thumbs div{width:100px;height:66px;background:linear-gradient(160deg,#efe7dc,#c7b2d8)}
.info{left:765px;top:10px;width:440px}
.crumb{font-size:13px;color:#333}.crumb em{font-style:normal;color:#a5661e;font-weight:500}
.info h1{font-family:Prata,serif;font-weight:400;font-size:33px;margin-top:14px}
.stock{font-size:13px;color:var(--green);margin-top:22px}
.price{font-size:36px;margin-top:10px}.price small{font-size:14px;color:#a5661e;margin-left:8px}
.qty{margin-top:12px;width:150px;height:50px;border:1px solid #ccc;display:flex;align-items:center;justify-content:space-between;padding:0 10px;font-size:20px}
.qty i{width:36px;height:34px;background:var(--gold);color:#fff;font-style:normal;display:flex;align-items:center;justify-content:center;font-size:24px}
.info p{font-size:14.5px;line-height:24px;color:#333;margin-top:14px}
.btn{display:inline-flex;align-items:center;justify-content:center;color:#fff;font-family:Hind,sans-serif;font-size:23px}
.tabs{left:120px;top:742px;width:1200px;height:450px;background:#fff;border:1px solid #e4e4e4}
.tabbar{height:66px;border-bottom:1px solid #e6e6e6;position:relative;font-size:25px}
.tabbar .t1{position:absolute;left:10px;top:20px;width:200px;text-align:center;color:var(--gold-text);border-bottom:3px solid var(--gold-text);height:46px}
.tabbar .t2{position:absolute;left:266px;top:24px}
.desc{padding:22px 40px;font-size:14.5px;line-height:24px;color:#333;width:860px}
.desc p{margin-bottom:24px}
.desc ul{margin:0 0 24px 26px}
.h2{font-family:Hind,sans-serif;color:var(--gold-text);font-size:31px;font-weight:500}
.card{top:1280px;width:320px;height:500px;background:#fff;text-align:center}
.card .img{position:absolute;left:30px;top:50px;width:260px;height:240px}
.card .stars{position:absolute;top:316px;left:0;width:100%;font-size:14px;color:#333}
.card .stars b{color:var(--star);letter-spacing:3px;font-size:17px;font-weight:400;margin-right:10px}
.card h3{position:absolute;top:358px;width:100%;font-weight:400;font-size:18.5px;line-height:26px}
.card .acts{position:absolute;top:440px;width:100%;display:flex;justify-content:center;gap:6px}
.contact{left:120px;top:1862px;width:1200px;height:385px;background:#fff}
.map{left:164px;top:22px;width:500px;height:340px;background:linear-gradient(135deg,#e6e8e4,#d9dee0);border-radius:14px}
.contact h2{position:absolute;left:784px;top:16px;font-family:Prata,serif;font-weight:400;font-size:37px;color:var(--gold-text)}
.field{position:absolute;left:784px;width:300px;height:34px;border:2px solid var(--gold);font-size:15px;color:#666;padding:6px 8px}
.footer{left:120px;top:2268px;width:1200px;height:238px;background:#fff}
.footer h4{position:absolute;top:22px;font-family:Hind,sans-serif;font-weight:500;font-size:22px;color:var(--gold-text)}
.footer .ln{position:absolute;font-size:16px;color:#222;line-height:30px}
.pay{position:absolute;width:40px;height:32px;background:#2b2b2b;border-radius:3px}
.soc{position:absolute;top:2326px;width:30px;height:30px;border-radius:50%;background:#222}
.legal{left:0;top:2506px;width:1440px;height:50px;background:var(--brown);color:#fff;font-size:12px;display:flex;justify-content:center;align-items:center;gap:22px}
</style>
</head>
<body>
<div class="page">
  <header class="abs topbar">
    <span style="left:120px"><svg width="26" height="22" viewBox="0 0 26 22"><path d="M2 6l7-3 8 3 7-3v13l-7 3-8-3-7 3z" fill="#fff"/></svg>Find Our Stores</span>
    <span style="left:954px;top:30px"><svg width="20" height="22" viewBox="0 0 20 22"><circle cx="10" cy="6" r="5" fill="#fff"/><path d="M1 22c0-7 4-9 9-9s9 2 9 9z" fill="#fff"/></svg>Login</span>
    <span style="left:1078px;top:30px"><svg width="28" height="22" viewBox="0 0 28 22"><circle cx="10" cy="6" r="5" fill="#fff"/><path d="M1 22c0-7 4-9 9-9s9 2 9 9z" fill="#fff"/><path d="M22 5v8M18 9h8" stroke="#fff" stroke-width="2.5"/></svg>Sign Up</span>
    <span style="left:1234px;top:30px"><svg width="26" height="22" viewBox="0 0 26 22"><path d="M1 2h4l3 12h13l3-9H7" fill="none" stroke="#fff" stroke-width="2.5"/><circle cx="10" cy="19" r="2" fill="#fff"/><circle cx="19" cy="19" r="2" fill="#fff"/></svg><em class="badge">0</em>Cart</span>
  </header>
  <nav class="abs mainnav">
    <div class="abs brand">Marlow</div>
    <div class="abs menu"><span>OUR CHOCOLATES<i>▼</i></span><span>SPECIAL EVENTS<i>▼</i></span><span>GIFTS &amp; HAMPERS<i>▼</i></span><span>ABOUT US</span></div>
  </nav>

  <section class="abs product">
    <aside class="abs cats">
      <div class="head">Shop by Categories</div>
      <div class="g">Chocolates<b>▼</b></div>
      <div class="g">Gifts &amp; Chocolate Hampers<b>▲</b></div>
      <div class="d">Gifts Boxes</div>
      <div class="d">Snack Bags</div>
      <div class="g">Special Events<b>▼</b></div>
    </aside>
    <div class="abs hero" role="img" aria-label="Photo of a wicker hamper filled with chocolate boxes and treats"></div>
    <div class="abs dots"><i></i><i class="on"></i><i></i><i></i></div>
    <div class="abs thumbs" role="img" aria-label="Thumbnail photos of the hamper from different angles"><div></div><div></div><div></div><div></div></div>
    <div class="abs info">
      <div class="crumb">Home &gt; Products &gt; <em>Chocolate Gift Hampers</em></div>
      <h1>Chocolate Gift Hampers</h1>
      <div class="stock">In stock | <svg width="16" height="11" viewBox="0 0 16 11"><path d="M0 0h10v8H0zM10 3h4l2 3v2h-6z" fill="#3aa43a"/><circle cx="3" cy="9" r="2" fill="#3aa43a"/><circle cx="12" cy="9" r="2" fill="#3aa43a"/></svg> Ships Now</div>
      <div class="price">$99<small>Free Delivery over $35</small></div>
      <div class="qty"><i>−</i>1<i>+</i></div>
      <p><b style="font-weight:500">FREE delivery on hampers for Sydney Metro residents.<br>Hamper shipping for residents outside Sydney Metro is $26.50.</b><br>Marlow chocolate gift hampers make the perfect present for loved ones, for clients, for those in need of a pick me up or simply to say, “thank you.”</p>
      <div style="margin-top:10px;display:flex;gap:10px"><span class="btn" style="width:170px;height:45px;background:var(--gold)">Add to Cart</span><span class="btn" style="width:170px;height:45px;background:var(--maroon)">Buy Now</span></div>
    </div>
  </section>

  <section class="abs tabs">
    <div class="tabbar"><span class="t1">Description</span><span class="t2">Reviews</span></div>
    <div class="desc">
      <p>Bringing together some of our favourite handcrafted chocolate bonbons, you’ll find many a chocolate treat to please your palate. From fruit filled, to refreshing mints and ginger to decadent caramels, our chocolate hampers will bring Marlow’ legendary Sydney chocolates to your doorstep.</p>
      <div>All our chocolate hampers are:</div>
      <ul><li>GLUTEN FREE</li><li>PALM OIL FREE</li><li>Our chocolates are made with 95% Australian ingredients</li></ul>
      <p>Nothing says that you care like a handcrafted Marlow chocolate hamper. They make perfect chocolate gift and they’re the best way to sample our very best Sydney chocolates.</p>
      <p>Find your favourite handmade chocolate in Sydney’s best chocolate gift hamper from Marlow – handcrafting delicious chocolates from our factory since 1932. Order yours today to taste the difference!</p>
    </div>
  </section>

  <h2 class="abs h2" style="left:118px;top:1218px">Related Products</h2>
  <article class="abs card" style="left:133px">
    <div class="img" role="img" aria-label="Cream gift box with red ribbon" style="background:linear-gradient(160deg,#f3ead2,#e0cfa8);height:140px;top:80px"></div>
    <div class="stars"><b>★★★★★</b>398</div>
    <h3>Marlow Gold Box 275g<br>$28.38</h3>
    <div class="acts"><span class="btn" style="width:46px;height:46px;background:var(--gold)"><svg width="24" height="22" viewBox="0 0 26 22"><path d="M1 2h4l3 12h13l3-9H7" fill="none" stroke="#fff" stroke-width="2.5"/><circle cx="10" cy="19" r="2" fill="#fff"/><circle cx="19" cy="19" r="2" fill="#fff"/></svg></span><span class="btn" style="width:150px;height:46px;background:var(--gold)">Buy Now</span></div>
  </article>
  <article class="abs card" style="left:567px">
    <div class="img" role="img" aria-label="Red gift box with white bow" style="background:linear-gradient(160deg,#e0434c,#c8202a);height:205px;top:45px"></div>
    <div class="stars"><b>★★★★★</b>198</div>
    <h3>Marlow Selection Box 550g Red<br>$49.50</h3>
    <div class="acts"><span class="btn" style="width:46px;height:46px;background:var(--gold)"><svg width="24" height="22" viewBox="0 0 26 22"><path d="M1 2h4l3 12h13l3-9H7" fill="none" stroke="#fff" stroke-width="2.5"/><circle cx="10" cy="19" r="2" fill="#fff"/><circle cx="19" cy="19" r="2" fill="#fff"/></svg></span><span class="btn" style="width:150px;height:46px;background:var(--gold)">Buy Now</span></div>
  </article>
  <article class="abs card" style="left:1000px">
    <div class="img" role="img" aria-label="Dark gift bag of nut clusters" style="background:linear-gradient(180deg,#1d1f2c 55%,#b01822);width:110px;left:116px;top:40px;height:250px"></div>
    <div class="stars"><b>★★★★★</b>298</div>
    <h3>Wander Nut Clusters 150g<br>$9.99</h3>
    <div class="acts"><span class="btn" style="width:46px;height:46px;background:var(--gold)"><svg width="24" height="22" viewBox="0 0 26 22"><path d="M1 2h4l3 12h13l3-9H7" fill="none" stroke="#fff" stroke-width="2.5"/><circle cx="10" cy="19" r="2" fill="#fff"/><circle cx="19" cy="19" r="2" fill="#fff"/></svg></span><span class="btn" style="width:150px;height:46px;background:var(--gold)">Buy Now</span></div>
  </article>
  <span class="abs btn" style="left:605px;top:1800px;width:230px;height:40px;background:var(--gold);border-radius:20px;font-size:20px">View More Products</span>

  <section class="abs contact">
    <div class="abs map" role="img" aria-label="Street map showing the Marlow Confections shop location"></div>
    <h2>Let keep in touch</h2>
    <div class="field" style="top:82px">Full Name</div>
    <div class="field" style="top:133px">Email Address</div>
    <div class="field" style="top:184px">Mobile no</div>
    <div class="field" style="top:235px;height:70px">Give Your Feedback</div>
    <span class="abs btn" style="left:784px;top:323px;width:175px;height:40px;background:var(--gold);font-size:20px">Submit</span>
  </section>

  <footer class="abs footer">
    <h4 style="left:4px">Contact us</h4>
    <svg class="abs" style="left:6px;top:66px" width="22" height="110" viewBox="0 0 22 110"><path d="M3 4h16v4l-4 2v4H7v-4L3 8z" fill="#222"/><path d="M2 30h18v12H2z M2 30l9 7 9-7" fill="none" stroke="#222" stroke-width="2"/><path d="M11 58a6 6 0 0 1 6 6c0 5-6 11-6 11s-6-6-6-11a6 6 0 0 1 6-6z" fill="none" stroke="#222" stroke-width="2.5"/></svg>
    <div class="ln" style="left:49px;top:50px">+61 2 9000 4417<br>hello@marlowconfections.com.au<br>48 Wattle Lane, Hollybrook<br>NSW, Australia</div>
    <h4 style="left:429px">Explore</h4>
    <div class="ln" style="left:430px;top:50px">About us<br>Long In<br>Sign Up<br>Track My Order<br>View Products</div>
    <h4 style="left:669px">Secure Payments</h4>
    <div class="pay" style="left:669px;top:58px"></div><div class="pay" style="left:725px;top:58px"></div><div class="pay" style="left:780px;top:58px"></div>
    <div class="pay" style="left:669px;top:112px"></div><div class="pay" style="left:725px;top:112px"></div>
    <h4 style="left:979px">Follow us</h4>
  </footer>
  <span class="soc" style="left:1100px;background:var(--maroon)"></span><span class="soc" style="left:1144px"></span><span class="soc" style="left:1187px"></span><span class="soc" style="left:1231px"></span>
  <div class="abs legal"><span>Privacy Policy</span><span>Shipping Policy</span><span>Terms &amp; Conditions</span><span>Copyrights © 2020 Marlow Confections</span></div>
</div>
</body>
</html>
```